Software allocation system needs a business card design

We need a business card designed for our software platform - www.tolvexa.com.au

At the moment the logo and website is all black and white, we are happy for suggestions on implementing some colour throughout either the logo or business card.

Industry/Entity Type

Software

Font styles to use
Sans Serif

Colors

Designer to choose colors to be used in the design.

```html
<!DOCTYPE html>
<html lang="en">
<head>
<meta charset="utf-8">
<title>Tolvexa Business Card</title>
<link href="https://fonts.googleapis.com/css2?family=Lato:wght@300;400&display=swap" rel="stylesheet">
<style>
  :root {
    --backdrop: #e9e6e1;
    --card: #fbfbfb;
    --ink: #1a1a1a;
    --ink-soft: #444444;
    --ink-muted: #6d6d6d;
  }
  * { margin: 0; padding: 0; box-sizing: border-box; }
  html, body {
    width: 1200px; height: 1023px; overflow: hidden;
    background: var(--backdrop);
    font-family: "Lato", Arial, sans-serif;
  }
  .stage {
    width: 1200px; height: 1023px;
    display: flex; align-items: center; justify-content: center;
  }
  .business-card {
    position: relative;
    width: 840px; height: 480px;
    background: var(--card);
    border-radius: 22px;
    box-shadow: 0 10px 30px rgba(0,0,0,0.15);
    color: var(--ink);
  }
  .brand {
    position: absolute; left: 64px; top: 86px;
    display: flex; align-items: center; gap: 18px;
  }
  .brand-dot {
    width: 44px; height: 44px; border-radius: 50%;
    background: var(--ink);
  }
  .brand-name {
    font-weight: 300; font-size: 70px; letter-spacing: 6px;
    color: var(--ink); line-height: 1;
  }
  .person { position: absolute; left: 130px; top: 196px; }
  .person-name {
    font-weight: 300; font-size: 30px; letter-spacing: 1.5px;
    color: var(--ink-soft); text-transform: uppercase;
  }
  .person-role {
    font-weight: 400; font-size: 16px; color: var(--ink-muted);
    margin-top: 6px;
  }
  .contact-list {
    position: absolute; left: 130px; top: 300px;
    list-style: none;
  }
  .contact-item {
    display: flex; align-items: center; gap: 12px;
    font-size: 18px; color: var(--ink-muted); font-weight: 400;
    margin-bottom: 8px;
  }
  .contact-icon {
    width: 18px; height: 18px; border-radius: 3px;
    background: var(--ink-muted);
    display: flex; align-items: center; justify-content: center;
  }
  .address {
    position: absolute; left: 130px; top: 420px;
    font-size: 18px; color: var(--ink-muted);
  }
</style>
</head>
<body>
<main class="stage">
  <article class="business-card">
    <div class="brand">
      <span class="brand-dot"></span>
      <span class="brand-name">TOLVEXA</span>
    </div>
    <div class="person">
      <p class="person-name">Rowan Pelletier</p>
      <p class="person-role">Director</p>
    </div>
    <ul class="contact-list">
      <li class="contact-item">
        <span class="contact-icon">
          <svg width="12" height="12" viewBox="0 0 12 12"><rect x="3" y="1" width="6" height="10" rx="1" fill="none" stroke="#fff" stroke-width="1.3"/><circle cx="6" cy="9" r="0.7" fill="#fff"/></svg>
        </span>041 5283 906
      </li>
      <li class="contact-item">
        <span class="contact-icon">
          <svg width="12" height="12" viewBox="0 0 12 12"><path d="M3 1.5l2 2.2-1 1.3a6 6 0 0 0 3 3l1.3-1 2.2 2-1 1.5C5.5 10.5 1.5 6.5 1.5 2.5z" fill="#fff"/></svg>
        </span>097 3126 458
      </li>
      <li class="contact-item">
        <span class="contact-icon">
          <svg width="12" height="12" viewBox="0 0 12 12"><rect x="1.5" y="3" width="9" height="6" fill="none" stroke="#fff" stroke-width="1.2"/><path d="M1.5 3l4.5 3.5L10.5 3" fill="none" stroke="#fff" stroke-width="1.2"/></svg>
        </span>rowanp@tolvexa.com.au
      </li>
    </ul>
    <p class="address">PO Box 512, Harbour Vale NSW 2291</p>
  </article>
</main>
</body>
</html>
```